Professional, Elegant, Modern and Playful stationery design for an Orthodontist (Dentist)

We need a new stationery design for an Orthodontist (Dentist).
We would like to see designs that are elegant, but also playful. The designs and colors should be in harmony with the existing logo (uploaded).
The font of the logo text is roboto (Google), you don't need to use the same font, but the used font has to be in harmony with the font used in the logo and it has to be usable in Microsoft Word.
The colors used have to be in harmony with the logo.
The design for following parts are needed:
- A4 letter paper design
- A4 Microsoft Word Template (with and without letterhead)
- Envelope designs for C4 and C5 with the window on the right side
- CD/DVD-label design
- Stamping design

Target Market(s)

Orthodontist (Dentist)

Industry/Entity Type

It Professional

Font styles to use
Sans Serif

Colors

Designer to choose colors to be used in the design.

Requirements
Must have
• * Logo files are uploaded
• * A4 letter paper design: for printing press
• - Address position is on the right side
• - Needed Information in the letterhead:
• - Logo with company name as a unit
• or
• - separate the logo from the text and position them separately
• - Text needed:
• Kieferorthopädie Sonnhalde
• Dr. med. dent. Till Brösecke
• Fachzahnarzt für Kieferorthopädie (CH)
• Eidg. dipl. Zahnarzt, Mitglied VFP und BZR
• Wendelhofweg 7
• 8964 Talwil
• 044 518 27 40
• (fax:)
• 044 518 27 41
• info@zahnbogen-praxis.example
• www.zahnbogen-praxis.example
• * A4 Microsoft Word Templates:
• - an empty and undesigned text example template is uploaded
• - the address lines are already correctly positioned behind the envelope window
• - design the positions of all elements
• - choose suitable fonts, which are in harmony with the font in the logo and the letterhead and which can be used in Microsoft Word (compatible with latest version, no old versions (.doc) needed)
• - choose suitable font sizes weights and colors, which are in harmony with the font in the logo and the letterhead.
• - One version with letterhead for printing on an empty paper
• - One version without letterhead for printing on a paper with letterhead already printed in printing press
• * Envelopes C4 and C5
• - window on the right side
• - Logo with company name (see uploaded files) as a unit
• or
• - Text needed:
• Wendelhofweg 7
• 8964 Talwil
• * DVD/CD-label:
• or
• - Text needed:
• Wendelhofweg 7
• 8964 Talwil
• 044 518 27 40
• info@zahnbogen-praxis.example
• www.zahnbogen-praxis.example
• - Patient name with birth date:
• Doe John, *1.2.1999
• - Two lines of text describing the contents on the CD/DVD
• * Stamping design:
• - Logo
• - Text:
• Kieferorthopädie Sonnhalde GmbH
• Wendelhofweg 7
• 8964 Talwil
Should not have
• - Old Microsoft Word versions (.doc)

```html
<!DOCTYPE html>
<html lang="de">
<head>
<meta charset="utf-8">
<title>Kieferorthopädie Sonnhalde – Stationery</title>
<link href="https://fonts.googleapis.com/css2?family=Roboto:wght@400;500;700&display=swap" rel="stylesheet">
<style>
:root{
  --navy:#08076a;
  --blue:#1aa7e6;
  --guide:#8fd6f2;
  --cut:#e79ac4;
  --magenta:#e0117f;
  --ink:#555a63;
  --ink-soft:#7b8089;
  --paper:#ffffff;
  --flap:#f1f1f2;
  --stage:#f3f3f4;
}
*{box-sizing:border-box;margin:0;padding:0}
html,body{width:1200px;height:1200px;overflow:hidden;background:var(--stage)}
body{position:relative;font-family:'Roboto',Arial,sans-serif;color:var(--ink)}
.sheet{position:absolute;background:var(--paper);box-shadow:0 6px 18px rgba(0,0,0,.12);overflow:hidden}
.guide{position:absolute;border:1px dashed var(--guide)}
.wave{position:absolute;left:0;bottom:0;width:100%}
.brand-name{color:var(--navy);font-weight:700;line-height:1.1}
.brand-sub{color:var(--navy);font-weight:400;line-height:1.25}
.brand-dot{display:inline-block;border-radius:50%;background:var(--navy)}
.contacts{position:absolute;list-style:none}
.contacts li{display:flex;align-items:center;gap:5px;white-space:nowrap}
.ico{width:6px;height:6px;fill:var(--navy);flex:none}
.center{text-align:center;left:0;right:0;position:absolute}

/* letter with letterhead */
.letter-full{left:63px;top:58px;width:365px;height:516px}
.letter-full .brand{position:absolute;left:50px;top:39px;display:flex;gap:7px;align-items:flex-start}
.letter-full .brand .brand-dot{width:12px;height:12px;margin-top:2px}
.letter-full .brand-name{font-size:10px}
.letter-full .brand-sub{font-size:6.6px}
.letter-full .date{position:absolute;left:45px;top:99px;font-size:8.4px}
.letter-full .sender{position:absolute;left:218px;top:100px;width:110px;text-align:center;font-size:5.6px;line-height:1.4;color:var(--ink-soft)}
.letter-full .subject{position:absolute;left:45px;top:120px;font-size:12px;color:var(--blue)}
.letter-full .body{position:absolute;left:45px;width:276px;font-size:5.7px;line-height:10.4px;text-align:justify}
.letter-full .salute{top:156px}
.letter-full .text{top:177px}
.letter-full .closing{top:302px}
.letter-full .sign{top:345px}
.letter-full .contacts{left:240px;top:423px;font-size:6px;line-height:11.2px}

/* letter template */
.letter-plain{left:495px;top:58px;width:365px;height:516px}
.letter-plain .brand-dot{position:absolute;left:176px;top:30px;width:14px;height:14px}
.letter-plain .name{top:78px;font-size:10px}
.letter-plain .subs{top:91px;font-size:6.8px}
.letter-plain .sender{top:114px;font-size:7px;line-height:1.45;color:var(--ink)}

/* CD label */
.disc{position:absolute;left:925px;top:82px;width:208px;height:208px;border-radius:50%;background:var(--paper);box-shadow:0 6px 18px rgba(0,0,0,.12)}
.disc .ring{position:absolute;border-radius:50%;border:1px dashed var(--guide)}
.disc .hub{position:absolute;left:86px;top:86px;width:36px;height:36px;border-radius:50%;border:1px solid #f08b8b}
.disc .name{top:153px;font-size:10px}

/* folder */
.folder-left{left:677px;top:350px;width:237px;height:254px}
.folder-left .guide{left:15px;top:24px;width:208px;height:206px}
.folder-left .sender{top:106px;font-size:7.8px;line-height:1.45}
.folder-left .contacts{left:0;right:0;top:140px;font-size:6.8px;line-height:18px;display:flex;flex-wrap:wrap;justify-content:center;column-gap:14px}
.folder-left .contacts li.web{flex-basis:100%;justify-content:center}
.folder-right{left:914px;top:330px;width:237px;height:294px}
.folder-right .guide{left:15px;top:18px;width:208px;height:230px}
.folder-right .brand-dot{position:absolute;left:110px;top:44px;width:16px;height:16px}
.folder-right .name{top:97px;font-size:10.5px}
.folder-right .subs{top:111px;font-size:7.4px}
.folder-right .label{top:150px;font-size:8.6px;font-weight:500;letter-spacing:.2px;color:#4a4f58}
.folder-right .patient{position:absolute;left:62px;top:170px;width:112px;height:18px;background:#ececee;border-radius:2px}
.folder-right .rule{position:absolute;left:51px;top:197px;width:125px;height:1px;background:#9ea2a8}

/* envelopes */
.envelope{position:absolute;overflow:visible}
.envelope svg.die{position:absolute;left:0;top:0;filter:drop-shadow(0 5px 10px rgba(0,0,0,.12))}
.envelope .format{position:absolute;font-size:5.6px;font-weight:700;color:var(--magenta)}
.envelope .brand{position:absolute;display:flex;gap:6px;align-items:flex-start}
.envelope .address{position:absolute;font-size:5px;line-height:8.2px;color:var(--ink)}
.envelope .contacts{font-size:5px;line-height:9px}
.envelope .ico{width:5px;height:5px}
.env-c4{left:66px;top:640px;width:600px;height:510px}
.env-c4 .brand{left:187px;top:98px}
.env-c4 .brand-dot{width:12px;height:12px;margin-top:1px}
.env-c4 .brand-name{font-size:9.6px}
.env-c4 .brand-sub{font-size:6.4px}
.env-c4 .format{left:276px;top:70px}
.env-c4 .address{left:346px;top:348px}
.env-c4 .contacts{left:346px;top:392px}
.env-c5{left:736px;top:674px;width:376px;height:480px}
.env-c5 .brand{left:55px;top:82px}
.env-c5 .brand-dot{width:10px;height:10px;margin-top:1px}
.env-c5 .brand-name{font-size:7.6px}
.env-c5 .brand-sub{font-size:5px}
.env-c5 .format{left:148px;top:57px}
.env-c5 .address{left:50px;top:132px}
.env-c5 .contacts{left:260px;top:198px}
</style>
</head>
<body>

<svg width="0" height="0" style="position:absolute" aria-hidden="true">
  <defs>
    <symbol id="i-fax" viewBox="0 0 10 10"><rect x="2.5" y="0.5" width="5" height="3" /><rect x="0.5" y="3.5" width="9" height="4.5" rx="1"/><rect x="2.5" y="7" width="5" height="2.5"/></symbol>
    <symbol id="i-phone" viewBox="0 0 10 10"><path d="M2 1 L4 1 L4.6 3.2 L3.4 4.2 Q4.6 6 5.8 6.6 L6.8 5.4 L9 6 L9 8 Q9 9 8 9 Q1 8.5 1 2 Q1 1 2 1Z"/></symbol>
    <symbol id="i-mail" viewBox="0 0 10 10"><path d="M0.5 2 H9.5 V8 H0.5Z M1.3 2.6 L5 5.4 L8.7 2.6" fill="none" stroke="#08076a" stroke-width="1.2"/></symbol>
    <symbol id="i-web" viewBox="0 0 10 10"><circle cx="5" cy="5" r="4.5"/><path d="M2 4 Q4 3 5 5 Q6 7 8 6" fill="none" stroke="#fff" stroke-width="0.9"/></symbol>
  </defs>
</svg>

<!-- A4 letter with letterhead -->
<section class="sheet letter-full" aria-label="A4 Briefpapier">
  <div class="guide" style="left:45px;top:44px;width:276px;height:427px"></div>
  <div class="brand">
    <span class="brand-dot"></span>
    <div>
      <div class="brand-name">Kieferorthopädie Sonnhalde</div>
      <div class="brand-sub">Dr. med. dent. Till Brösecke</div>
      <div class="brand-sub">Fachzahnarzt für Kieferorthopädie (CH)</div>
    </div>
  </div>
  <div class="date">Talwil, 30.3.2017</div>
  <div class="sender">Eidg. dipl. Zahnarzt,<br>Mitglied VFP und BZR<br>Wendelhofweg 7,<br>8964 Talwil</div>
  <div class="subject">Subject</div>
  <p class="body salute">Sehr geehrte Damen und Herren</p>
  <p class="body text">Lorem ipsum dolor sit amet, consectetuer adipiscing elit, sed diam nonummy nibh euismod tincidunt ut laoreet dolore magna aliquam erat volutpat. Ut wisi enim ad minim veniam, quis nostrud exerci tation ullamcorper suscipit lobortis nisl ut aliquip ex ea commodo consequat. Duis autem vel eum iriure dolor in hendrerit in vulputate velit esse molestie conorem ipsum dolor sit amet, consectetuer adipiscing elit, sed diam nonummy nibh euismod tincidunt ut laoreet dolore magna aliquam erat volutpat. Ut wisi enim ad minim veniam, quis nostrud exerci tation ullamcorper suscipit lobortis nisl ut aliquip ex ea commodo consequat. Duis autem vel eum iriure dolor in hendrerit in vulputate velit esse molestie con</p>
  <p class="body closing">Freundliche Grüsse</p>
  <p class="body sign">Till Brösecke,<br>Dr. med. dent.,<br>Fachzahnarzt für Kieferorthopädie (CH)</p>
  <ul class="contacts">
    <li><svg class="ico"><use href="#i-fax"/></svg>+ 044 518 27 41</li>
    <li><svg class="ico"><use href="#i-phone"/></svg>+ 044 518 27 40</li>
    <li><svg class="ico"><use href="#i-mail"/></svg>info@zahnbogen-praxis.example</li>
    <li><svg class="ico"><use href="#i-web"/></svg>www.zahnbogen-praxis.example</li>
  </ul>
  <svg class="wave" viewBox="0 0 365 44" height="44" preserveAspectRatio="none" aria-hidden="true">
    <path d="M0 8 C90 -2 190 30 365 10 L365 44 L0 44Z" fill="var(--navy)"/>
    <path d="M0 5 C90 -5 190 26 365 7" fill="none" stroke="var(--blue)" stroke-width="2"/>
  </svg>
</section>

<!-- A4 Word template -->
<section class="sheet letter-plain" aria-label="A4 Word-Vorlage">
  <div class="guide" style="left:45px;top:44px;width:276px;height:427px"></div>
  <span class="brand-dot"></span>
  <div class="center brand-name name">Kieferorthopädie Sonnhalde</div>
  <div class="center brand-sub subs">Dr. med. dent. Till Brösecke<br>Fachzahnarzt für Kieferorthopädie (CH)</div>
  <div class="center sender">Eidg. dipl. Zahnarzt, Mitglied VFP und BZR<br>Wendelhofweg 7, 8964 Talwil</div>
  <svg class="wave" viewBox="0 0 365 44" height="44" preserveAspectRatio="none" aria-hidden="true">
    <path d="M0 8 C90 -2 190 30 365 10 L365 44 L0 44Z" fill="var(--navy)"/>
    <path d="M0 5 C90 -5 190 26 365 7" fill="none" stroke="var(--blue)" stroke-width="2"/>
  </svg>
</section>

<!-- CD / DVD label -->
<section class="disc" aria-label="CD/DVD-Label">
  <div class="ring" style="left:8px;top:8px;width:192px;height:192px"></div>
  <div class="ring" style="left:62px;top:62px;width:84px;height:84px"></div>
  <div class="hub"></div>
  <div class="center brand-name name">Kieferorthopädie Sonnhalde</div>
</section>

<!-- Folder, left panel -->
<section class="sheet folder-left" aria-label="Mappe Rückseite">
  <div class="guide"></div>
  <div class="center sender">Eidg. dipl. Zahnarzt, Mitglied VFP und BZR<br>Wendelhofweg 7, 8964 Talwil</div>
  <ul class="contacts">
    <li><svg class="ico"><use href="#i-phone"/></svg>+ 044 518 27 40</li>
    <li><svg class="ico"><use href="#i-mail"/></svg>info@zahnbogen-praxis.example</li>
    <li class="web"><svg class="ico"><use href="#i-web"/></svg>www.zahnbogen-praxis.example</li>
  </ul>
</section>

<!-- Folder, right panel -->
<section class="sheet folder-right" aria-label="Mappe Vorderseite">
  <div class="guide"></div>
  <span class="brand-dot"></span>
  <div class="center brand-name name">Kieferorthopädie Sonnhalde</div>
  <div class="center brand-sub subs">Dr. med. dent. Till Brösecke<br>Fachzahnarzt für Kieferorthopädie (CH)</div>
  <div class="center label">PATIENT NAME WITH BIRTH DATE:</div>
  <div class="patient" role="img" aria-label="Handgeschriebener Patientenname mit Geburtsdatum: Doe John, *1.2.1999"></div>
  <div class="rule"></div>
  <svg class="wave" viewBox="0 0 237 66" height="66" preserveAspectRatio="none" aria-hidden="true">
    <path d="M0 26 C60 10 130 36 237 12 L237 66 L0 66Z" fill="var(--navy)"/>
    <path d="M0 23 C60 7 130 32 237 8" fill="none" stroke="var(--blue)" stroke-width="2.2"/>
  </svg>
</section>

<!-- C4 envelope -->
<section class="envelope env-c4" aria-label="Couvert C4">
  <svg class="die" width="600" height="510" viewBox="0 0 600 510" aria-hidden="true">
    <path d="M12 68 Q0 68 0 80 L0 460 Q0 470 12 470 L143 470 L143 456 L158 456 L158 69 L150 68Z" fill="var(--flap)" stroke="var(--cut)" stroke-width=".7"/>
    <path d="M588 68 Q600 68 600 80 L600 460 Q600 470 588 470 L460 470 L460 456 L442 456 L442 69 L450 68Z" fill="var(--flap)" stroke="var(--cut)" stroke-width=".7"/>
    <rect x="12" y="134" width="138" height="307" fill="#fff" stroke="var(--guide)" stroke-width=".7"/>
    <rect x="450" y="134" width="138" height="307" fill="#fff" stroke="var(--guide)" stroke-width=".7"/>
    <path d="M158 69 L168 22 Q172 12 185 11 L300 8 L415 11 Q428 12 432 22 L442 69Z" fill="#fff" stroke="var(--cut)" stroke-width=".7"/>
    <path d="M164 69 L173 24 Q176 16 187 15 L300 12 L413 15 Q424 16 427 24 L436 69" fill="none" stroke="var(--guide)" stroke-width=".7"/>
    <rect x="158" y="69" width="284" height="390" fill="#fff" stroke="var(--cut)" stroke-width=".7"/>
    <rect x="162" y="73" width="276" height="383" fill="none" stroke="var(--guide)" stroke-width=".7"/>
    <rect x="293" y="154" width="125" height="56" rx="2" fill="#efeff0"/>
    <path d="M134 438 C220 420 330 460 440 440 C470 434 490 440 500 446 L430 446 L424 470 Q420 510 398 510 L180 510 Q160 510 158 478 L150 452Z" fill="var(--navy)"/>
    <path d="M150 444 C230 423 330 462 440 440" fill="none" stroke="var(--blue)" stroke-width="2"/>
  </svg>
  <div class="format">229mm x 324mm</div>
  <div class="brand">
    <span class="brand-dot"></span>
    <div>
      <div class="brand-name">Kieferorthopädie Sonnhalde</div>
      <div class="brand-sub">Dr. med. dent. Till Brösecke</div>
      <div class="brand-sub">Fachzahnarzt für Kieferorthopädie (CH)</div>
    </div>
  </div>
  <div class="address">Address:<br>Eidg. dipl. Zahnarzt,<br>Mitglied VFP und BZR<br>Wendelhofweg 7,<br>8964 Talwil</div>
  <ul class="contacts">
    <li><svg class="ico"><use href="#i-fax"/></svg>+ 044 518 27 41</li>
    <li><svg class="ico"><use href="#i-phone"/></svg>+ 044 518 27 40</li>
    <li><svg class="ico"><use href="#i-mail"/></svg>info@zahnbogen-praxis.example</li>
    <li><svg class="ico"><use href="#i-web"/></svg>www.zahnbogen-praxis.example</li>
  </ul>
</section>

<!-- C5 envelope -->
<section class="envelope env-c5" aria-label="Couvert C5">
  <svg class="die" width="376" height="480" viewBox="0 0 376 480" aria-hidden="true">
    <path d="M34 55 L8 55 Q0 56 0 66 L0 262 L34 262Z" fill="var(--flap)" stroke="var(--cut)" stroke-width=".7"/>
    <path d="M342 55 L368 55 Q376 56 376 66 L376 262 L342 262Z" fill="var(--flap)" stroke="var(--cut)" stroke-width=".7"/>
    <path d="M34 55 L46 12 Q49 3 60 3 L316 3 Q327 3 330 12 L342 55Z" fill="#fff" stroke="var(--cut)" stroke-width=".7"/>
    <path d="M40 55 L50 14 Q53 7 62 7 L314 7 Q323 7 326 14 L336 55" fill="none" stroke="var(--guide)" stroke-width=".7"/>
    <rect x="34" y="55" width="308" height="210" fill="#fff" stroke="var(--cut)" stroke-width=".7"/>
    <rect x="38" y="59" width="300" height="200" fill="none" stroke="var(--guide)" stroke-width=".7"/>
    <rect x="192" y="124" width="136" height="60" rx="2" fill="#efeff0"/>
    <path d="M2 264 C80 236 180 266 280 258 C330 254 360 250 376 244 L376 262 L352 272 Q346 290 346 310 L346 466 Q346 480 332 480 L46 480 Q34 480 34 466 L34 300 Q32 280 2 268Z" fill="var(--navy)"/>
    <path d="M34 250 C110 238 200 266 290 256 C330 252 360 248 376 242" fill="none" stroke="var(--blue)" stroke-width="2"/>
  </svg>
  <div class="format">229mm x 162mm</div>
  <div class="brand">
    <span class="brand-dot"></span>
    <div>
      <div class="brand-name">Kieferorthopädie Sonnhalde</div>
      <div class="brand-sub">Dr. med. dent. Till Brösecke</div>
      <div class="brand-sub">Fachzahnarzt für Kieferorthopädie (CH)</div>
    </div>
  </div>
  <div class="address">Address:<br>Eidg. dipl. Zahnarzt,<br>Mitglied VFP und BZR<br>Wendelhofweg 7,<br>8964 Talwil</div>
  <ul class="contacts">
    <li><svg class="ico"><use href="#i-fax"/></svg>+ 044 518 27 41</li>
    <li><svg class="ico"><use href="#i-phone"/></svg>+ 044 518 27 40</li>
    <li><svg class="ico"><use href="#i-mail"/></svg>info@zahnbogen-praxis.example</li>
    <li><svg class="ico"><use href="#i-web"/></svg>www.zahnbogen-praxis.example</li>
  </ul>
</section>

</body>
</html>
```